Meadowlark Learning Support Partners (MLSP)

This is a professional business card. Logo and picture are a must on the front of the card. I am an educational consultant. I have been consulting for the past three years for a company. I am now opening my own company. My goal for my consulting company is to eventually consult all over America.

Target Market(s)

Educators, schools, professionals

Industry/Entity Type

Consulting

Contact Information for Business Card

Picture/logo on front, simple modern design

Font styles to use
Serif

Colors
85abd2
0355a3
3176b5
cedeed

Requirements
Must have
• picture, logo,
• Dorotea Halvorsen, Ed.S
• address 5327 Quarry ridge Ln. Nashville, TN 37058
• Cell:616-555-0182
• Office: 629-555-0147
• www.Mlspwx.com
• halvorsendorotea@mailvexo.com

```html
<!DOCTYPE html>
<html lang="en">
<head>
<meta charset="utf-8">
<title>Meadowlark Learning Support Partners – Business Card</title>
<link href="https://fonts.googleapis.com/css2?family=Baloo+2:wght@600&family=Roboto:wght@400&display=swap" rel="stylesheet">
<style>
  :root {
    --page-bg: #e7e4df;
    --card-top: #f4f0ea;
    --card-top-end: #ebe6de;
    --navy: #1c3c6a;
    --band-blue: #1e4274;
    --band-blue-deep: #173661;
    --strip-dark: #2c2b33;
    --ink: #2b2b2b;
    --white: #ffffff;
    --address: #e2d3c8;
    --photo-light: #cfc7ba;
    --photo-dark: #34343e;
  }
  html, body {
    margin: 0;
    width: 1200px;
    height: 1054px;
    overflow: hidden;
    background: var(--page-bg);
  }
  .business-card {
    position: absolute;
    left: 100px;
    top: 225px;
    width: 1000px;
    height: 603px;
    overflow: hidden;
    border-radius: 6px;
    background: linear-gradient(180deg, var(--card-top), var(--card-top-end));
    box-shadow: 0 10px 30px rgba(0,0,0,.18);
    font-family: "Roboto", Arial, sans-serif;
  }
  .card-band {
    position: absolute;
    left: 0; top: 308px;
    width: 1000px; height: 295px;
    background: linear-gradient(90deg, var(--band-blue-deep), var(--band-blue));
  }
  .card-strip {
    position: absolute;
    left: 0; top: 534px;
    width: 1000px; height: 69px;
  }
  .holder-name {
    position: absolute;
    left: 45px; top: 76px;
    margin: 0;
    font-family: "Baloo 2", Georgia, serif;
    font-weight: 600;
    font-size: 34px;
    line-height: 1;
    color: var(--navy);
  }
  .holder-title {
    position: absolute;
    left: 46px; top: 131px;
    margin: 0;
    font-size: 21px;
    color: var(--ink);
  }
  .brand {
    position: absolute;
    left: 612px; top: 58px;
    display: flex;
    align-items: center;
    gap: 22px;
  }
  .brand-mark {
    width: 64px; height: 64px;
    border-radius: 50%;
    background: var(--navy);
    flex: none;
  }
  .brand-name {
    margin: 0;
    font-family: "Baloo 2", Georgia, serif;
    font-weight: 600;
    font-size: 25px;
    line-height: 33px;
    color: var(--navy);
  }
  .contact-list {
    position: absolute;
    left: 48px; top: 348px;
    margin: 0; padding: 0;
    list-style: none;
  }
  .contact-item {
    display: flex;
    align-items: center;
    height: 34.5px;
    font-size: 24px;
    color: var(--white);
  }
  .contact-icon {
    width: 22px; height: 22px;
    margin-right: 20px;
    flex: none;
  }
  .address {
    position: absolute;
    left: 38px; top: 548px;
    margin: 0;
    font-size: 23px;
    color: var(--address);
  }
  .portrait {
    position: absolute;
    left: 661px; top: 229px;
    width: 339px; height: 350px;
    background: linear-gradient(180deg, var(--photo-light) 0%, #b9ab96 45%, var(--photo-dark) 100%);
  }
</style>
</head>
<body>
  <section class="business-card">
    <div class="card-band"></div>
    <svg class="card-strip" viewBox="0 0 1000 69" aria-hidden="true">
      <path d="M0 0 H585 C602 0 602 42 622 42 H1000 V69 H0 Z" fill="var(--strip-dark)"/>
    </svg>

    <h1 class="holder-name">Dorotea Halvorsen, Ed.S</h1>
    <p class="holder-title">Managing Director</p>

    <div class="brand">
      <span class="brand-mark"></span>
      <p class="brand-name">Meadowlark<br>Learning<br>Support<br>Partners</p>
    </div>

    <ul class="contact-list">
      <li class="contact-item">
        <svg class="contact-icon" viewBox="0 0 24 24" aria-hidden="true"><rect x="6" y="2" width="12" height="20" rx="2" fill="none" stroke="#fff" stroke-width="2"/><circle cx="12" cy="18" r="1.3" fill="#fff"/></svg>
        616-555-0182
      </li>
      <li class="contact-item">
        <svg class="contact-icon" viewBox="0 0 24 24" aria-hidden="true"><path d="M3 9 C3 4 21 4 21 9 L17 10 L16 7.5 H8 L7 10 Z" fill="#fff"/><rect x="5" y="12" width="14" height="9" rx="2" fill="#fff"/></svg>
        629-555-0147
      </li>
      <li class="contact-item">
        <svg class="contact-icon" viewBox="0 0 24 24" aria-hidden="true" fill="none" stroke="#fff" stroke-width="1.8"><circle cx="12" cy="12" r="9"/><ellipse cx="12" cy="12" rx="4" ry="9"/><path d="M3 12 H21"/></svg>
        www.Mlspwx.com
      </li>
      <li class="contact-item">
        <svg class="contact-icon" viewBox="0 0 24 24" aria-hidden="true"><rect x="2" y="5" width="20" height="14" rx="1" fill="#fff"/><path d="M2 6 L12 13 L22 6" fill="none" stroke="var(--band-blue)" stroke-width="1.8"/></svg>
        halvorsendorotea@mailvexo.com
      </li>
    </ul>

    <p class="address">5327 Quarry ridge Ln. Nashville, TN 37058</p>

    <div class="portrait" role="img" aria-label="Portrait photo of Dorotea Halvorsen"></div>
  </section>
</body>
</html>
```